Brell Harbor Company Business Cards

Front and Back Business Card - logo and text setup - cool design. I need workable photoshop or illustrator files so I can setup each employee card with design that is created
Updates

Hi everyone, thank you for the great entries. Please no more white and blue cards - there are so many already - black and silver only now please. thanks!

Target Market(s)

Construction Industry - Facility Managers

Industry/Entity Type

Construction

Contact Information for Business Card

I really like contemporary simplistic looks - clean neat....not opposed to seeing some black backrounds

Requirements
Must have
• Logo/website address with design on front only - www.brellharbor-example.com (logo attached)
• Back:
• Name/Title/Company Address/Phone/email address
Nice to have
• Cool design
Should not have
• Nothing gimmicky like Fire or Water - since we are a Fire Protection company - it has all been done

```html
<!DOCTYPE html>
<html lang="en">
<head>
<meta charset="utf-8">
<title>Brell Harbor Company – Business Cards</title>
<link rel="stylesheet" href="https://fonts.googleapis.com/css2?family=Maven+Pro:wght@400;500;700&display=swap">
<style>
  :root {
    --backdrop: #1b1b1b;
    --card-dark: #161616;
    --card-silver: #e4e5e7;
    --silver: #b9bcc0;
    --silver-deep: #8c9095;
    --black: #111111;
    --ink: #222222;
    --pale: #e4e4e4;
  }
  * { margin: 0; padding: 0; box-sizing: border-box; }
  html, body {
    width: 1200px; height: 1000px; overflow: hidden;
    background: var(--backdrop);
    font-family: "Maven Pro", sans-serif;
  }
  .canvas { position: relative; width: 1200px; height: 1000px; }

  .card { position: absolute; left: 276px; width: 648px; }

  /* Front */
  .card-front {
    top: 86px; height: 372px;
    background: var(--card-dark);
  }
  .front-name {
    position: absolute; top: 170px; left: 0; width: 100%;
    text-align: center;
    font-size: 26px; line-height: 32px; font-weight: 700; letter-spacing: 1px;
    color: var(--silver);
  }
  .front-url {
    position: absolute; top: 326px; left: 0; width: 100%;
    text-align: center;
    font-size: 14px; line-height: 18px; letter-spacing: 5px;
    color: var(--pale);
  }

  /* Back */
  .card-back {
    top: 532px; height: 370px;
    background: var(--card-silver);
    color: var(--ink);
  }
  .company-name {
    position: absolute; left: 45px; top: 38px;
    font-size: 36px; font-weight: 700;
    color: var(--black);
    letter-spacing: -0.5px;
  }
  .person {
    position: absolute; right: 46px; top: 144px;
    text-align: right;
  }
  .person-name { font-size: 23px; line-height: 28px; letter-spacing: 0.5px; }
  .person-name .first { font-weight: 700; color: var(--black); }
  .person-name .last { font-weight: 400; color: var(--silver-deep); }
  .person-title { font-size: 15px; line-height: 18px; }
  .person-title .org { color: var(--silver-deep); }

  .divider {
    position: absolute; left: 45px; right: 46px; top: 206px;
    height: 1px; background: var(--black);
  }

  .contacts { position: absolute; left: 45px; top: 220px; list-style: none; }
  .contacts li {
    display: flex; align-items: center;
    height: 26px; margin-bottom: 1px;
    font-size: 16px;
  }
  .contacts li:nth-child(2) { margin-bottom: 0; margin-top: 2px; }
  .contacts svg { width: 18px; height: 18px; margin-right: 9px; fill: var(--black); flex: none; }

  .address {
    position: absolute; right: 46px; top: 270px;
    text-align: right; font-size: 16px; line-height: 28px;
  }

  .footer-band { position: absolute; left: 0; bottom: 0; width: 648px; height: 14px; }
</style>
</head>
<body>
<main class="canvas">

  <section class="card card-front" aria-label="Card front">
    <div class="front-name">Brell Harbor Company</div>
    <div class="front-url">WWW.BRELLHARBOR-EXAMPLE.COM</div>
  </section>

  <section class="card card-back" aria-label="Card back">
    <div class="company-name">Brell Harbor</div>

    <div class="person">
      <div class="person-name"><span class="first">MAREK</span> <span class="last">OLSEN</span></div>
      <div class="person-title">CEO of <span class="org">Brell Harbor</span></div>
    </div>

    <div class="divider"></div>

    <ul class="contacts">
      <li>
        <svg viewBox="0 0 24 24" aria-hidden="true"><path d="M6.6 10.8a15.1 15.1 0 0 0 6.6 6.6l2.2-2.2c.3-.3.7-.4 1-.2 1.1.4 2.3.6 3.6.6.6 0 1 .4 1 1V20c0 .6-.4 1-1 1A17 17 0 0 1 3 4c0-.6.4-1 1-1h3.5c.6 0 1 .4 1 1 0 1.3.2 2.5.6 3.6.1.3 0 .7-.2 1z"/></svg>
        (02) 5550 1427
      </li>
      <li>
        <svg viewBox="0 0 24 24" aria-hidden="true"><path d="M7 1h10a2 2 0 0 1 2 2v18a2 2 0 0 1-2 2H7a2 2 0 0 1-2-2V3a2 2 0 0 1 2-2zm0 3v14h10V4zm5 15.5a1.2 1.2 0 1 0 0 2.4 1.2 1.2 0 0 0 0-2.4z"/></svg>
        0400 555 218
      </li>
      <li>
        <svg viewBox="0 0 24 24" aria-hidden="true"><path d="M2 5h20v2l-10 6L2 7zm0 4.3l10 6 10-6V19H2z"/></svg>
        info@brellharbor-example.com
      </li>
      <li>
        <svg viewBox="0 0 24 24" aria-hidden="true"><path d="M12 2a10 10 0 1 0 0 20 10 10 0 0 0 0-20zm-1 17.9A8 8 0 0 1 4.2 10L9 14.8v1a2 2 0 0 0 2 2zm6.9-2.5a2 2 0 0 0-1.9-1.4h-1v-3a1 1 0 0 0-1-1H8v-2h2a1 1 0 0 0 1-1V7h2a2 2 0 0 0 2-2v-.4a8 8 0 0 1 2.9 12.8z"/></svg>
        www.brellharbor-example.com
      </li>
    </ul>

    <div class="address">
      18 Quarry Lane, Westmere<br>
      NSW 2199
    </div>

    <svg class="footer-band" viewBox="0 0 648 14" aria-hidden="true">
      <polygon points="0,0 487,0 482,14 0,14" fill="var(--black)"/>
      <polygon points="494,0 648,0 648,14 489,14" fill="var(--silver-deep)"/>
    </svg>
  </section>

</main>
</body>
</html>
```